Forge Night Club Flyer, need asap for party this weekend

Text is drawn as an attachment

Need a flyer for club night this Saturday. Guaranteed project need quick turnaround. Image attached, and the FORGE logo to be large and detailed like a sign. The dj names KESTREL, MR. HALVORNE, AND DESMOND K. ORLEY can be large too. It's for house/electronic music in a nice classy venue. High Res image attached.

Target Market(s)

21-40 year old house music lovers, club business

Industry/Entity Type

Night Club

Font styles to use
Sans Serif

Colors
ffffff
cadf82
33a6d7
0356a4
fbee3d

Requirements
Must have
• Either the girl in hard hat or tool belt image, or something similar to stick with the Forge theme. Also the dj names needs to be the same size
Nice to have
• Faded image or some lining around the images so it doesn't look like a plain photo. Black and white is good or faded.
Should not have
• Any cursive or anything not professional looking

```html
<!DOCTYPE html>
<html lang="en">
<head>
<meta charset="utf-8">
<title>Forge – Electronic Music Night</title>
<link rel="stylesheet" href="https://fonts.googleapis.com/css2?family=Russo+One&family=Saira+Condensed:wght@600;700&family=Oswald:wght@500;600&family=Orbitron:wght@600;700&display=swap">
<style>
  :root {
    --blue-deep: #0356a4;
    --blue-bright: #1f6fd6;
    --blue-sky: #33a6d7;
    --ink: #05070c;
    --white: #ffffff;
    --gold-light: #fbee3d;
    --gold-mid: #f5b400;
    --gold-deep: #e88a00;
    --date-yellow: #fbee3d;
    --photo-skin: #c99a78;
    --photo-belt: #d9a12b;
    --photo-denim: #3e5a78;
  }
  * { margin: 0; padding: 0; box-sizing: border-box; }
  html, body { width: 1200px; height: 907px; overflow: hidden; background: var(--blue-deep); }

  .flyer {
    position: relative;
    width: 1200px;
    height: 907px;
    overflow: hidden;
    background:
      radial-gradient(ellipse 520px 420px at 62% 45%, var(--blue-sky) 0%, rgba(51,166,215,0) 70%),
      radial-gradient(ellipse 420px 520px at 100% 60%, rgba(5,7,12,0.85) 0%, rgba(5,7,12,0) 75%),
      linear-gradient(160deg, var(--blue-bright) 0%, var(--blue-deep) 55%, #022c5c 100%);
  }

  .flyer__photo {
    position: absolute;
    left: 0; top: 0;
    width: 560px; height: 907px;
    background:
      linear-gradient(180deg, #8c3a3a 0%, #8c3a3a 11%, var(--photo-skin) 14%, var(--photo-skin) 48%, var(--photo-belt) 52%, var(--photo-belt) 86%, var(--photo-denim) 90%, var(--photo-denim) 100%);
    -webkit-mask-image: linear-gradient(90deg, #000 78%, transparent 100%);
            mask-image: linear-gradient(90deg, #000 78%, transparent 100%);
  }

  .flyer__content {
    position: absolute;
    left: 560px; top: 0;
    width: 600px; height: 907px;
    text-align: center;
  }

  .headline,
  .genre,
  .venue {
    position: absolute;
    left: 0; width: 600px;
    white-space: nowrap;
    line-height: 1;
  }

  .headline {
    top: 70px;
    font-family: "Russo One", sans-serif;
    font-size: 140px;
    letter-spacing: 4px;
    background: linear-gradient(180deg, var(--gold-light) 0%, var(--gold-mid) 50%, var(--gold-deep) 100%);
    -webkit-background-clip: text;
            background-clip: text;
    color: transparent;
  }

  .genre {
    top: 228px;
    font-family: "Saira Condensed", sans-serif;
    font-weight: 700;
    font-size: 80px;
    color: var(--white);
    letter-spacing: 1px;
  }

  .venue {
    top: 334px;
    font-family: "Saira Condensed", sans-serif;
    font-weight: 700;
    font-size: 58px;
    background: linear-gradient(180deg, var(--gold-light) 0%, var(--gold-mid) 55%, var(--gold-deep) 100%);
    -webkit-background-clip: text;
            background-clip: text;
    color: transparent;
  }

  .lineup {
    position: absolute;
    top: 444px; left: 0; width: 600px;
    list-style: none;
    font-family: "Oswald", sans-serif;
    font-weight: 600;
    font-size: 42px;
    line-height: 64px;
    color: var(--white);
    display: flex;
    flex-wrap: wrap;
    justify-content: center;
    column-gap: 34px;
  }
  .lineup__artist { white-space: nowrap; }
  .lineup__artist::before {
    content: "";
    display: inline-block;
    width: 20px; height: 20px;
    border-radius: 50%;
    background: var(--gold-mid);
    margin-right: 8px;
    vertical-align: 6px;
  }

  .when {
    position: absolute;
    left: 560px; top: 630px;
    width: 600px; height: 190px;
    background: linear-gradient(180deg, #1a1d24 0%, var(--ink) 100%);
    border: 3px solid #3a3f4a;
    border-radius: 14px;
    box-shadow: 0 0 18px rgba(255,255,255,0.25);
    display: flex;
    flex-direction: column;
    justify-content: center;
    align-items: center;
    gap: 12px;
  }
  .when__date {
    font-family: "Saira Condensed", sans-serif;
    font-weight: 700;
    font-size: 66px;
    line-height: 1;
    color: var(--date-yellow);
    white-space: nowrap;
  }
  .when__time {
    font-family: "Orbitron", sans-serif;
    font-weight: 700;
    font-size: 46px;
    line-height: 1;
    letter-spacing: 2px;
    color: var(--date-yellow);
    white-space: nowrap;
  }
</style>
</head>
<body>
  <main class="flyer">
    <div class="flyer__photo" role="img" aria-label="Photo of a woman in a knotted plaid shirt and denim shorts wearing a leather tool belt with wrenches, pliers and a hammer"></div>

    <section class="flyer__content">
      <h1 class="headline">FORGE</h1>
      <p class="genre">ELECTRONIC MUSIC</p>
      <p class="venue">IN A NICE CLASSY VENUE</p>
      <ul class="lineup">
        <li class="lineup__artist">KESTREL</li>
        <li class="lineup__artist">MR. HALVORNE</li>
        <li class="lineup__artist">DESMOND K. ORLEY</li>
      </ul>
    </section>

    <div class="when">
      <p class="when__date">3RD DEC 2016</p>
      <p class="when__time">10PM TO 2 AM</p>
    </div>
  </main>
</body>
</html>
```